Zielgruppe
Strandhaus mit Restaurant (Beach feeling)
Zielgruppe: gehoben, edel, teuer
Aufgabenstellung
Auf stilsicherheit und das es stylisch und gleichzeitig edel aussieht.
Format:
Breite 44,5
Höher 71
Text:
Logo oben gut sichtbar
Herzlich Willkommen! (andere Schriftart)
MONTAG - FREITAG
SAMSTAG - SONNTAG
Unsere Küche verwöhnt dich bis 21:00 Uhr - täglich frisch & mit Liebe gekocht.
Wolkenstrand ist mehr als ein Ort - es ist ein Gefühl. (andere Schriftart)
Lindmoor, Falkner Str. 58-60, 2794 Wiener Neustadt
www.wolkenstrand-beispiel.at/reservieren

```html
<!DOCTYPE html>
<html lang="de">
<head>
<meta charset="utf-8">
<title>Wolkenstrand – Herzlich Willkommen</title>
<link rel="stylesheet" href="https://fonts.googleapis.com/css2?family=Kaushan+Script&family=Kalam&family=Oswald:wght@500;600&display=swap">
<style>
  :root {
    --page: #ffffff;
    --paper: #eeeeee;
    --ink: #1f6dbf;
    --shell-faint: #d6dcee;
    --shell-mid: #8ea8da;
    --shell-deep: #6f8fcf;
  }
  html, body {
    margin: 0;
    width: 1200px;
    height: 1200px;
    overflow: hidden;
    background: var(--page);
  }
  .poster {
    position: absolute;
    left: 279px;
    top: 86px;
    width: 648px;
    height: 1034px;
    background: var(--paper);
    overflow: hidden;
    color: var(--ink);
    text-align: center;
    box-shadow: 0 6px 24px rgba(0,0,0,0.18);
  }
  .art { position: absolute; }
  .art--conch {
    left: 30px; top: -20px; width: 640px; height: 284px;
    background: radial-gradient(ellipse at 35% 45%, rgba(214,220,238,0.95), rgba(214,220,238,0.55) 65%, rgba(214,220,238,0) 100%);
    border-radius: 30% 0 70% 45% / 40% 0 100% 60%;
  }
  .art--whelk {
    left: -10px; top: 615px; width: 128px; height: 177px;
    background: radial-gradient(ellipse at 45% 45%, var(--shell-deep), rgba(142,168,218,0.55) 75%, rgba(142,168,218,0.2));
    border-radius: 40% 55% 50% 45% / 45% 50% 55% 50%;
  }
  .art--murex {
    left: 546px; top: 598px; width: 112px; height: 178px;
    background: radial-gradient(ellipse at 55% 50%, var(--shell-deep), rgba(142,168,218,0.55) 75%, rgba(142,168,218,0.2));
    border-radius: 55% 40% 30% 60% / 50% 45% 55% 50%;
    transform: rotate(-12deg);
  }
  .art--cone {
    left: 140px; top: 750px; width: 159px; height: 78px;
    background: linear-gradient(100deg, rgba(142,168,218,0.35), rgba(142,168,218,0.75));
    border-radius: 50% 30% 50% 60% / 55% 50% 50% 45%;
    transform: rotate(12deg);
  }
  .art--clam {
    left: 39px; top: 807px; width: 151px; height: 119px;
    background: radial-gradient(ellipse at 40% 35%, rgba(142,168,218,0.4), rgba(111,143,207,0.8));
    border-radius: 50% 50% 45% 45% / 60% 60% 40% 40%;
  }
  .art--spiral {
    left: 237px; top: 786px; width: 191px; height: 144px;
    background: radial-gradient(circle at 62% 42%, rgba(111,143,207,0.85), rgba(142,168,218,0.55) 45%, rgba(142,168,218,0.3) 80%);
    border-radius: 60% 55% 50% 40% / 60% 55% 45% 40%;
  }
  .art--auger {
    left: 452px; top: 757px; width: 75px; height: 163px;
    background: linear-gradient(180deg, rgba(142,168,218,0.4), rgba(111,143,207,0.8));
    border-radius: 50% 50% 50% 50% / 75% 75% 25% 25%;
    transform: rotate(25deg);
  }
  .art--scallop {
    left: 555px; top: 801px; width: 110px; height: 169px;
    background: radial-gradient(ellipse at 50% 90%, rgba(111,143,207,0.85), rgba(142,168,218,0.45));
    border-radius: 50% 50% 45% 45% / 55% 55% 45% 45%;
  }
  .brand {
    position: absolute;
    left: 0; right: 0; top: 120px;
    margin: 0;
    font-family: "Kaushan Script", cursive;
    font-weight: 400;
    font-size: 52px;
    line-height: 1;
  }
  .brand__dot {
    display: inline-block;
    width: 10px; height: 10px;
    border-radius: 50%;
    background: var(--ink);
    vertical-align: middle;
    margin-left: 10px;
  }
  .welcome {
    position: absolute;
    left: 0; right: 0; top: 236px;
    margin: 0;
    font-family: "Kaushan Script", cursive;
    font-weight: 400;
    font-size: 98px;
    line-height: 88px;
  }
  .hours {
    position: absolute;
    left: 0; right: 0; top: 433px;
    margin: 0;
  }
  .hours__days {
    font-family: "Kaushan Script", cursive;
    font-size: 28px;
    line-height: 38px;
  }
  .hours__time {
    font-family: "Oswald", sans-serif;
    font-weight: 600;
    font-size: 32px;
    line-height: 42px;
    margin-bottom: 5px;
  }
  .note {
    position: absolute;
    left: 0; right: 0; top: 611px;
    margin: 0;
    font-family: "Kalam", cursive;
    font-size: 19px;
    line-height: 26px;
    transform: skewX(-8deg);
  }
  .address {
    position: absolute;
    left: 0; right: 0; top: 944px;
    margin: 0;
    font-family: "Oswald", sans-serif;
    font-style: normal;
    font-weight: 500;
    font-size: 15px;
    line-height: 23px;
    letter-spacing: 5px;
    text-transform: uppercase;
  }
</style>
</head>
<body>
  <main class="poster">
    <div class="art art--conch" role="img" aria-label="Große, zarte Linienzeichnung einer Muschel in hellem Blau"></div>

    <h1 class="brand">Wolkenstrand<span class="brand__dot"></span></h1>

    <h2 class="welcome">Herzlich<br>Willkommen!</h2>

    <section class="hours">
      <div class="hours__days">Montag - Freitag</div>
      <div class="hours__time">11:00 - 00:00</div>
      <div class="hours__days">Samstag - Sonntag</div>
      <div class="hours__time">09:00 - 00:00</div>
    </section>

    <div class="art art--whelk" role="img" aria-label="Gezeichnete Meeresschnecke in Blau"></div>
    <div class="art art--murex" role="img" aria-label="Gezeichnete Stachelschnecke in Blau"></div>

    <p class="note">
      Unsere Küche verwöhnt dich bis<br>
      21:00 Uhr - täglich frisch &amp; mit Liebe gekocht.<br>
      Wolkenstrand ist mehr als ein Ort<br>
      - es ist ein Gefühl.
    </p>

    <div class="art art--cone" role="img" aria-label="Gezeichnete Kegelschnecke in Blau"></div>
    <div class="art art--clam" role="img" aria-label="Gezeichnete Venusmuschel in Blau"></div>
    <div class="art art--spiral" role="img" aria-label="Gezeichnete Spiralschnecke in Blau"></div>
    <div class="art art--auger" role="img" aria-label="Gezeichnete Turmschnecke in Blau"></div>
    <div class="art art--scallop" role="img" aria-label="Gezeichnete Jakobsmuschel in Blau"></div>

    <address class="address">
      Lindmoor, Falkner Str. 58-60<br>
      2794 Wiener Neustadt<br>
      www.wolkenstrand-beispiel.at/reservieren
    </address>
  </main>
</body>
</html>
```